Psychologist starting new business and needs a business card and possibly a logo to attract customer

I need a logo and business card for my new private practice as a Clinical Psychologist. The business will simply be called Maribel Ostrow Psychology". I'll be providing one on one therapy, mostly to male and female adult clients, and occasionally to children or adolescents. I'd like to see designs that include a small logo. I'd like it to have a professional feel to it. I'd like to convey a sense of warmth and caring. It could suggest the concept of two people working together towards a goal - but not necessarily. Colour wise, I'm not sure, except that I don't want it to have too much bright blue, which I think is a bit over-used in health logos. On the back I'd just like to see 3 or four lines to make appointments - each line would have one long line to write the date with a short line next to it on which to place the time.

```html
<!DOCTYPE html>
<html lang="en">
<head>
<meta charset="utf-8">
<title>Maribel Ostrow Psychology – Business Card</title>
<link href="https://fonts.googleapis.com/css2?family=Open+Sans:wght@400;700&display=swap" rel="stylesheet">
<style>
  :root {
    --backdrop: #1e4a2f;
    --card: #ffffff;
    --brand-green: #0f7a45;
    --ink: #1a1a1a;
    --rule: #6b6b6b;
  }
  * { margin: 0; padding: 0; box-sizing: border-box; }
  html, body { width: 1200px; height: 845px; overflow: hidden; }
  body {
    background: var(--backdrop);
    font-family: "Open Sans", Arial, sans-serif;
    position: relative;
  }
  .card {
    position: absolute;
    background: var(--card);
    border-radius: 40px;
  }
  .card--front {
    left: 40px; top: 30px;
    width: 773px; height: 453px;
    display: flex; flex-direction: column; align-items: center;
    padding-top: 56px;
  }
  .brand-mark {
    width: 190px; height: 190px;
    border-radius: 50%;
    background: var(--brand-green);
  }
  .brand-name {
    margin-top: 36px;
    color: var(--brand-green);
    font-weight: 700;
    text-align: center;
    text-transform: uppercase;
    line-height: 1.05;
  }
  .brand-name__person { display: block; font-size: 40px; letter-spacing: 2px; }
  .brand-name__role { display: block; font-size: 66px; letter-spacing: 1px; }

  .card--back {
    left: 487px; top: 440px;
    width: 663px; height: 387px;
  }
  .appointment-title {
    position: absolute; top: 28px; left: 0; width: 100%;
    text-align: center;
    font-size: 26px; font-weight: 700; color: var(--ink);
  }
  .appointment-row {
    position: absolute; left: 49px; width: 590px; height: 30px;
    font-size: 22px; font-weight: 700; color: var(--ink);
  }
  .appointment-row span { position: absolute; bottom: 2px; }
  .label-date { left: 0; }
  .label-time { left: 291px; }
  .rule { position: absolute; bottom: 0; border-bottom: 1.5px solid var(--rule); }
  .rule--date { left: 66px; width: 342px; }
  .rule--time { left: 428px; width: 162px; }

  .lockup-small {
    position: absolute; right: 22px; bottom: 22px;
    display: flex; align-items: center; gap: 10px;
  }
  .lockup-small .brand-mark { width: 58px; height: 58px; }
  .lockup-small .brand-name { margin-top: 0; text-align: left; }
  .lockup-small .brand-name__person { font-size: 14px; letter-spacing: 1px; }
  .lockup-small .brand-name__role { font-size: 22px; letter-spacing: 0; }
</style>
</head>
<body>
  <section class="card card--front" aria-label="Business card front">
    <div class="brand-mark" aria-hidden="true"></div>
    <h1 class="brand-name">
      <span class="brand-name__person">Maribel Ostrow</span>
      <span class="brand-name__role">Psychologist</span>
    </h1>
  </section>

  <section class="card card--back" aria-label="Appointment card back">
    <h2 class="appointment-title">APPOINTMENT</h2>

    <div class="appointment-row" style="top:70px">
      <span class="label-date">Date</span><i class="rule rule--date"></i>
      <span class="label-time">Time</span><i class="rule rule--time"></i>
    </div>
    <div class="appointment-row" style="top:125px">
      <span class="label-date">Date</span><i class="rule rule--date"></i>
      <span class="label-time">Time</span><i class="rule rule--time"></i>
    </div>
    <div class="appointment-row" style="top:181px">
      <span class="label-date">Date</span><i class="rule rule--date"></i>
      <span class="label-time">Time</span><i class="rule rule--time"></i>
    </div>
    <div class="appointment-row" style="top:236px">
      <span class="label-date">Date</span><i class="rule rule--date"></i>
      <span class="label-time">Time</span><i class="rule rule--time"></i>
    </div>

    <div class="lockup-small">
      <div class="brand-mark" aria-hidden="true"></div>
      <p class="brand-name">
        <span class="brand-name__person">Maribel Ostrow</span>
        <span class="brand-name__role">Psychologist</span>
      </p>
    </div>
  </section>
</body>
</html>
```